Online tuition webpage design needed

Hi,
We are starting up an online tuition website for non- English speakers wishing to take an QRAVE test.

The webpage must include a place for people to enroll online in the course.
The home page must have:
• room for a logo (coming shortly, blue in colour)
• different packages of online tuition and coinvy
• tool bar showing different pages
• perhaps a video, small pictures

This is my site currently:-

www.lernmarowebtutor.example

as you can see, I am not very sure how to create a website … The large logo is what I would like to use, but I project has not been finalized yet. Please note, I don’t like the logo being that large!

Sites that are similar to what I am doing and like the design of are:

http://www.quorvapath.example.au/fees

https://www.brantiq9.example/index.php

http://www.tutorhalvekmorris.example.uk/index.html

http://www.vorplaneexam.example/

One thing I need is a place for student s to enroll, and if possible, I would like to use plovix to create exercises for students.
Currently, my site is using sitequill. My preference is to use plovix for online activities. I am not sure if I can use both.
Thanks in advance

Target Market(s)

people wising to take an QRAVE test (English proficiency test)

Industry/Entity Type

Online

Colors
3276b5
0292cd

Requirements
Must have
• a place for enrollment and admin login for students
plovix
video
talvo, gatherly, chirrup logos
Nice to have
• a booking calender
Should not have
• too much clutter. must be clean and professional looking

```html
<!DOCTYPE html>
<html lang="en">
<head>
<meta charset="utf-8">
<title>QRAVE Online Tuition</title>
<link href="https://fonts.googleapis.com/css2?family=Open+Sans:wght@400;600;700;800&family=Fira+Sans:wght@500;600&display=swap" rel="stylesheet">
<style>
:root{
  --brand:#3276b5;
  --brand-bright:#0292cd;
  --sky:#0ea2ea;
  --ink:#3a3a3a;
  --muted:#666;
  --page:#f2f2f2;
  --white:#fff;
  --yellow:#f7e21a;
  --band:#1b1b1b;
  --footer:#3b4852;
  --price-1:#0b7dc0;
  --price-2:#0a69a6;
  --price-3:#05588a;
}
*{box-sizing:border-box;margin:0;padding:0}
html,body{width:780px;height:1200px;overflow:hidden}
body{position:relative;background:var(--page);font-family:"Open Sans",Arial,sans-serif;color:var(--ink)}
.abs{position:absolute}

/* header */
.site-header{left:0;top:0;width:780px;height:86px;background:var(--white);border-top:3px solid var(--brand)}
.brand{left:110px;top:12px;display:flex;align-items:center;gap:8px}
.brand-mark{width:30px;height:30px;background:var(--brand)}
.brand-name{font-size:34px;font-weight:600;color:var(--brand);line-height:1;letter-spacing:1px}
.brand-sub{left:180px;top:58px;font-size:13px;color:var(--brand);font-weight:600}
.main-nav{left:298px;top:0;display:flex;height:37px}
.main-nav a{font-size:8.5px;color:var(--brand-bright);text-decoration:none;text-transform:uppercase;padding:14px 6px 0;white-space:nowrap}
.main-nav a.active{background:var(--brand);color:var(--white);padding:14px 7px 0}
.login-btn{left:582px;top:70px;width:91px;height:16px;background:var(--brand);color:var(--white);font-size:8px;text-align:center;line-height:16px}

/* hero */
.hero{left:0;top:86px;width:780px;height:222px;background:radial-gradient(ellipse at 45% 40%,#c9b89a 0%,#8a7758 45%,#4d4232 100%);border-bottom:4px solid var(--brand)}
.hero-title{left:108px;top:120px;font-size:29px;font-weight:800;color:var(--yellow);line-height:35px;text-shadow:0 1px 2px rgba(0,0,0,.4)}
.hero-lead{left:108px;top:202px;font-size:17px;color:var(--white);line-height:32px;text-shadow:0 1px 2px rgba(0,0,0,.4)}
.hero-lead b{font-size:22px;font-weight:700}
.hero-photo{left:405px;top:111px;width:265px;height:161px;border:2px solid var(--brand);background:linear-gradient(160deg,#f4f4f4,#d9dde2 60%,#b8c2cc);box-shadow:0 6px 10px rgba(0,0,0,.35)}

/* skill cards */
.skill-card{top:342px;width:180px;height:173px;background:var(--white);border-bottom:3px solid #cfcfcf;text-align:center}
.skill-card svg{margin-top:18px}
.skill-card h3{font-size:12px;font-weight:400;color:var(--brand);margin-top:12px}
.skill-card p{font-size:8.5px;line-height:13px;color:var(--muted);margin:10px 12px 0}

/* enrol band */
.enrol-band{left:0;top:553px;width:780px;height:107px;background:repeating-linear-gradient(90deg,#1e1e1e 0 2px,#161616 2px 4px)}
.enrol-title{left:107px;top:574px;font-size:17px;color:var(--brand-bright);letter-spacing:.3px}
.enrol-text{left:108px;top:605px;width:410px;font-size:9.5px;color:var(--white);line-height:13px}
.enrol-btn{left:540px;top:591px;width:132px;height:32px;background:var(--brand-bright);border-left:4px solid var(--brand);color:var(--white);font-size:13px;line-height:32px;text-align:center}

/* video + testimonial */
.video{left:108px;top:688px;width:263px;height:138px;background:linear-gradient(135deg,#6b5a4a,#3a2e28 60%,#2a2422)}
.video-bar{left:108px;top:816px;width:263px;height:10px;background:#cfd3d6}
.section-title{left:396px;top:684px;font-size:14px;color:var(--brand)}
.slider-prev{left:636px;top:697px;width:17px;height:17px;background:#e4e4e4}
.slider-next{left:654px;top:697px;width:18px;height:17px;background:var(--brand-bright)}
.quote{left:396px;top:714px;width:276px;height:112px;background:var(--white);border-left:3px solid var(--brand)}
.quote-mark{left:410px;top:730px;font-size:64px;font-family:Georgia,serif;color:#d8d8d8;line-height:1;font-weight:700}
.quote-text{left:473px;top:743px;width:190px;font-size:9px;line-height:13px;color:var(--muted)}
.quote-name{left:473px;top:781px;font-size:7px;color:var(--brand-bright)}
.divider{left:108px;top:853px;width:564px;height:1px;background:var(--brand)}

/* pricing */
.plan{top:879px;width:175px;height:92px;font-family:"Fira Sans",Arial,sans-serif;color:var(--white);text-align:center}
.plan-name{height:54px;font-size:15px;font-weight:500;line-height:20px;padding-top:8px}
.plan-price{height:38px;background:var(--sky);font-size:23px;font-weight:600;line-height:38px}

/* footer */
.site-footer{left:0;top:998px;width:780px;height:202px;background:var(--footer);border-top:2px solid #20282e}
.foot-head{font-size:8px;color:var(--brand-bright);text-transform:uppercase}
.foot-links{left:108px;top:1045px;list-style:none;font-size:7.5px;color:var(--white);line-height:15.2px}
.foot-text{font-size:7.5px;color:var(--white);line-height:10px}
.social{left:410px;top:1046px;display:flex;gap:8px}
.social span{display:flex;flex-direction:column;align-items:center;gap:3px;font-size:6.5px;color:var(--white)}
.social i{display:block;width:24px;height:24px;background:var(--brand-bright)}
.calendar{left:531px;top:1024px;width:141px;height:151px;background:var(--white);padding:6px 8px;font-size:7.5px;color:#333}
.calendar caption{font-size:7.5px;padding:2px 0 6px;border-bottom:1px solid #ccc}
.calendar table{width:100%;border-collapse:collapse;text-align:center}
.calendar th{font-weight:600;padding:5px 0;border-bottom:1px solid #ccc}
.calendar td{padding:2.8px 0}
.calendar .cal-nav{font-size:6.5px;color:var(--brand);margin-top:4px;border-top:1px solid #ccc;padding-top:3px}
</style>
</head>
<body>

<header class="site-header abs"></header>
<div class="brand abs"><span class="brand-mark"></span><span class="brand-name">QRAVE</span></div>
<div class="brand-sub abs">Online Tuition</div>
<nav class="main-nav abs">
  <a class="active" href="#">Tutorial Packages</a>
  <a href="#">Tips &amp; Comments</a>
  <a href="#">Reading</a>
  <a href="#">Speaking</a>
  <a href="#">Listening</a>
  <a href="#">Writing</a>
</nav>
<div class="login-btn abs">Login &nbsp;/&nbsp; Register</div>

<section class="hero abs"></section>
<h1 class="hero-title abs">ONLINE<br>QRAVE TUITION</h1>
<p class="hero-lead abs">Professional help for people<br>taking an <b>QRAVE</b> test</p>
<div class="hero-photo abs" role="img" aria-label="Photo of a group of smiling students holding books and folders"></div>

<article class="skill-card abs" style="left:108px">
  <svg width="54" height="46" viewBox="0 0 54 46"><path d="M3 6h18c4 0 6 2 6 5v32c0-3-2-4-6-4H3z M51 6H33c-4 0-6 2-6 5v32c0-3 2-4 6-4h18z" fill="var(--brand)"/><path d="M6 9v27h15c2 0 4 .5 5 1.5V11c0-1.5-1.5-2-4-2z M48 9v27H33c-2 0-4 .5-5 1.5V11c0-1.5 1.5-2 4-2z" fill="var(--white)"/><path d="M9 12v21h13c1.5 0 2.5.3 3 .8V12.5c0-.3-1-.5-3-.5z M45 12v21H32c-1.5 0-2.5.3-3 .8V12.5c0-.3 1-.5 3-.5z" fill="var(--brand)"/></svg>
  <h3>READING</h3>
  <p>Lorem Ipsum is simply dummy text of the printing and typesetting industry. Lorem Ipsum has been the industry's</p>
</article>
<article class="skill-card abs" style="left:300px">
  <svg width="54" height="50" viewBox="0 0 54 50"><rect x="19" y="0" width="16" height="30" rx="8" fill="var(--brand)"/><path d="M13 22c0 9 6 14 14 14s14-5 14-14" stroke="var(--brand)" stroke-width="3" fill="none"/><rect x="25.5" y="36" width="3" height="8" fill="var(--brand)"/><rect x="18" y="44" width="18" height="3" fill="var(--brand)"/></svg>
  <h3 style="margin-top:8px">SPEAKING</h3>
  <p>Lorem Ipsum is simply dummy text of the printing and typesetting industry. Lorem Ipsum has been the industry's</p>
</article>
<article class="skill-card abs" style="left:492px">
  <svg width="54" height="46" viewBox="0 0 54 46"><path d="M5 32V25C5 12 14 3 27 3s22 9 22 22v7" stroke="var(--brand)" stroke-width="4" fill="none"/><rect x="3" y="25" width="12" height="20" rx="3" fill="var(--brand)"/><rect x="39" y="25" width="12" height="20" rx="3" fill="var(--brand)"/></svg>
  <h3>LISTENING</h3>
  <p>Lorem Ipsum is simply dummy text of the printing and typesetting industry. Lorem Ipsum has been the industry's</p>
</article>

<section class="enrol-band abs"></section>
<h2 class="enrol-title abs">LOREM IPSUM IS SIMPLY DUMMY</h2>
<p class="enrol-text abs">Lorem Ipsum is simply dummy text of the printing and typesetting industry. Lorem Ipsum has been the industry's standard dummy text ever since.</p>
<div class="enrol-btn abs">ENROLLMENT</div>

<div class="video abs" role="img" aria-label="Video still of a tutor speaking to the camera in a kitchen"></div>
<svg class="abs" style="left:217px;top:734px" width="46" height="30" viewBox="0 0 46 30"><ellipse cx="23" cy="15" rx="21" ry="13" fill="rgba(255,255,255,.25)" stroke="#fff" stroke-width="2"/><path d="M19 8l10 7-10 7z" fill="#fff"/></svg>
<div class="video-bar abs"></div>
<svg class="abs" style="left:110px;top:817px" width="259" height="8" viewBox="0 0 259 8"><circle cx="8" cy="4" r="3.5" fill="#555"/><path d="M7 2.5l2.5 1.5L7 5.5z" fill="#fff"/><rect x="16" y="3" width="130" height="2" fill="#888"/><rect x="148" y="0" width="50" height="8" fill="#444"/><text x="151" y="6.5" font-size="6" fill="#ddd" font-family="Open Sans,sans-serif">00:00 / 03:34</text><rect x="210" y="3" width="30" height="2" fill="#888"/><rect x="246" y="1" width="8" height="6" fill="#555"/></svg>

<h2 class="section-title abs">STUDENT SAYS</h2>
<svg class="slider-prev abs" viewBox="0 0 17 17"><path d="M10 5l-4 3.5 4 3.5" stroke="#999" stroke-width="1.5" fill="none"/></svg>
<svg class="slider-next abs" viewBox="0 0 18 17"><path d="M7 5l4 3.5-4 3.5" stroke="#fff" stroke-width="1.5" fill="none"/></svg>
<div class="quote abs"></div>
<div class="quote-mark abs">&ldquo;</div>
<p class="quote-text abs">Lorem Ipsum is simply dummy text of the printing and typesetting industry.</p>
<p class="quote-name abs">Mr. Lorem Ipsum</p>

<div class="divider abs"></div>

<div class="plan abs" style="left:108px;background:var(--price-1)"><div class="plan-name">1 MONTH<br>SUBSCRIPTION</div><div class="plan-price">ONLY $ 25</div></div>
<div class="plan abs" style="left:303px;background:var(--price-2)"><div class="plan-name">2 MONTH<br>SUBSCRIPTION</div><div class="plan-price">ONLY $ 25</div></div>
<div class="plan abs" style="left:497px;background:var(--price-3)"><div class="plan-name">3 MONTH<br>SUBSCRIPTION</div><div class="plan-price">ONLY $ 25</div></div>

<footer class="site-footer abs"></footer>
<h4 class="foot-head abs" style="left:108px;top:1024px">Quick Links</h4>
<ul class="foot-links abs">
  <li>Tutorial Packages</li><li>Tips &amp; Comments</li><li>Reading</li><li>Speaking</li><li>Listening</li><li>Writing</li><li>Enrollment</li><li>Login</li>
</ul>
<h4 class="foot-head abs" style="left:214px;top:1024px">Address</h4>
<p class="foot-text abs" style="left:212px;top:1044px">Lorem Ipsum is simply dummy text of the,<br>printing and typesetting industry,<br>Lorem Ipsum is simply,<br>dummy text of the printing.</p>
<svg class="abs" style="left:212px;top:1096px" width="10" height="10" viewBox="0 0 10 10"><path d="M2 1l2 2-1 1.5c.5 1 1.5 2 2.5 2.5L7 6l2 2-1.5 1.5C4.5 9 1 5.5.5 2.5z" fill="#fff"/></svg>
<p class="foot-text abs" style="left:228px;top:1096px">+91 00000 00000</p>
<svg class="abs" style="left:211px;top:1112px" width="11" height="8" viewBox="0 0 11 8"><rect width="11" height="8" fill="#fff"/><path d="M0 0l5.5 4.5L11 0" stroke="#3b4852" fill="none"/></svg>
<p class="foot-text abs" style="left:228px;top:1111px">hello@qravetutor.example</p>
<h4 class="foot-head abs" style="left:410px;top:1024px">Follow Us</h4>
<div class="social abs">
  <span><i></i>chirrup</span>
  <span><i></i>gatherly</span>
  <span><i></i>linkwise</span>
</div>

<div class="calendar abs">
  <table>
    <caption>JANUARY 2014</caption>
    <tr><th>M</th><th>T</th><th>W</th><th>T</th><th>F</th><th>S</th><th>S</th></tr>
    <tr><td></td><td></td><td>1</td><td>2</td><td>3</td><td>4</td><td>5</td></tr>
    <tr><td>6</td><td>7</td><td>8</td><td>9</td><td>10</td><td>11</td><td>12</td></tr>
    <tr><td>13</td><td>14</td><td>15</td><td>16</td><td>17</td><td>18</td><td>19</td></tr>
    <tr><td>20</td><td>21</td><td>22</td><td>23</td><td>24</td><td>25</td><td>26</td></tr>
    <tr><td>27</td><td>28</td><td>29</td><td>30</td><td>31</td><td></td><td></td></tr>
  </table>
  <div class="cal-nav">&laquo; Dec</div>
</div>

</body>
</html>
```